Microlight Aircraft Website Project

Need a website designed, or at least a template made, that my web programmer can work with here. We are a new manufacturer of microlight aircraft & powered hang gliders. Our company name is Brisk Fern. We manufacture portable utility aircraft in the Light Sport category (formerly known as Ultralights or Microlights). Our particular design is a 2-seat powered hang glider and caters to those who want to go explore the backcountry. We are not necessarily aviation nuts, but more into the development of a flying utility vehicle for extreme exploration and expeditions. We have been importing these aircraft from 3 countries for 15 years and have supplied over 200 expedition-quality aircraft world-wide. We are now manufacturing here in the US.

Industry/Entity Type

Manufacturer

Coding

Coded - Design and coding required

```html
<!DOCTYPE html>
<html lang="en">
<head>
<meta charset="utf-8">
<title>Brisk Fern — Microlight Aircraft</title>
<link rel="stylesheet" href="https://fonts.googleapis.com/css2?family=Lato:wght@300;400;700;900&display=swap">
<style>
:root{
  --navy:#0b4c9c;
  --navy-deep:#0a3f86;
  --cyan:#1cb0e6;
  --ink:#2d3440;
  --muted:#9aa1aa;
  --line:#e2e5ea;
  --panel:#e8edf3;
  --footer:#1f3147;
  --footer-text:#8f9bb0;
  --white:#ffffff;
}
*{box-sizing:border-box;margin:0;padding:0}
html,body{width:1200px;height:3273px;overflow:hidden}
body{font-family:'Lato',sans-serif;color:var(--ink);background:var(--white);position:relative}
.abs{position:absolute}
section,header,footer{position:absolute;left:0;width:1200px}

/* hero */
.hero{top:0;height:578px;overflow:hidden}
.hero-photo{position:absolute;inset:0;background:
  linear-gradient(160deg,#c7d3e2 0%,#eef2f7 30%,#b9c6d6 52%,#51627a 70%,#1e2b3d 100%)}
.topbar{position:absolute;top:0;left:0;width:1200px;height:35px;background:rgba(20,30,45,.55);color:var(--white);font-size:12px}
.topbar span{position:absolute;top:10px}
.topbar .dot{width:9px;height:9px;border-radius:50%;background:var(--white);top:13px}
.logo{position:absolute;left:192px;top:66px;display:flex;align-items:center;gap:10px}
.logo-mark{width:34px;height:34px;border-radius:50%;background:var(--navy)}
.logo-name{font-weight:900;font-size:26px;color:var(--navy);letter-spacing:.5px}
.nav{position:absolute;top:77px;left:563px;display:flex;gap:27px;font-size:12.5px;font-weight:700;color:var(--white);letter-spacing:.3px}
.hero-title{position:absolute;left:585px;top:198px;font-size:42px;font-weight:900;color:var(--navy)}

/* shared headings */
.sec-title{position:absolute;left:0;width:1200px;text-align:center;font-size:24px;font-weight:400;color:var(--navy);letter-spacing:.5px}
.sec-sub{position:absolute;left:0;width:1200px;text-align:center;font-size:11.5px;color:var(--muted)}
.divider{position:absolute;left:172px;width:856px;height:1px;background:var(--line)}
.divider i{position:absolute;left:420px;top:-7px;width:16px;height:14px;background:var(--white)}
.divider i::after{content:"";position:absolute;left:4px;top:3px;width:8px;height:8px;border:1px solid #c9ced6;transform:rotate(45deg)}

/* products */
.products{top:578px;height:578px}
.product{position:absolute;top:183px;width:271px;height:332px}
.product-photo{position:absolute;inset:0}
.product-name{position:absolute;bottom:14px;width:100%;text-align:center;color:var(--white);font-size:17px;line-height:23px;letter-spacing:.6px}

/* why choose us */
.why{top:1156px;height:470px;background:var(--panel)}
.why-photo{position:absolute;left:0;top:0;width:393px;height:470px;clip-path:polygon(0 0,100% 0,85% 100%,0 100%);
  background:linear-gradient(160deg,#e6c34a 0%,#6b8a56 35%,#3e6a44 70%,#27462f 100%)}
.why .sec-title{left:393px;width:807px;top:53px;font-size:20px;color:var(--ink)}
.why .sec-sub{left:393px;width:807px;top:88px;font-size:11px}
.why .divider{left:540px;width:370px;top:113px;background:#d5dbe3}
.feature{position:absolute;top:186px;width:194px;height:225px;background:var(--white);text-align:center}
.feature-icon{position:absolute;left:65px;top:-9px;width:64px;height:64px;border-radius:50%;background:var(--navy-deep)}
.feature h3{position:absolute;top:73px;width:100%;font-size:12.5px;font-weight:700;letter-spacing:.3px}
.feature .rule{position:absolute;top:97px;left:72px;width:50px;height:2px;background:var(--navy)}
.feature p{position:absolute;top:115px;left:24px;width:146px;font-size:11px;line-height:19px;color:#a7adb5}
.btn-sm{position:absolute;top:181px;left:59px;width:76px;height:22px;background:var(--navy-deep);color:var(--white);font-size:10.5px;font-weight:700;line-height:22px}

/* blog */
.blog{top:1626px;height:632px}
.blog .sec-title{top:36px}
.blog .sec-sub{top:76px}
.arrows{position:absolute;top:137px;left:974px;display:flex;gap:4px}
.arrows span{width:22px;height:22px;border:1px solid #d3d7dd;display:flex;align-items:center;justify-content:center}
.post{position:absolute;top:185px;width:271px;height:393px;background:#f3f4f6}
.post-photo{position:absolute;top:0;left:0;width:271px;height:203px}
.post-meta{position:absolute;top:203px;left:0;width:271px;height:37px;background:var(--cyan);color:var(--white);font-size:12px;line-height:37px;padding:0 18px;display:flex;justify-content:space-between}
.post h4{position:absolute;top:256px;left:15px;font-size:14px;font-weight:400;color:#333}
.post p{position:absolute;top:288px;left:15px;width:240px;font-size:11px;line-height:17px;color:#8f959e}
.post a{position:absolute;top:355px;left:15px;font-size:11px;color:var(--navy);text-decoration:none;font-weight:700}

/* banner */
.banner{top:2258px;height:103px;background:var(--navy);color:var(--white);text-align:center;font-size:18px;line-height:103px}

/* contact */
.contact{top:2361px;height:373px}
.contact-photo{position:absolute;left:0;top:0;width:680px;height:373px;
  background:linear-gradient(90deg,#a7b3c2 0%,#dfe6ee 40%,#f4f7fa 75%,rgba(255,255,255,0) 100%)}
.contact h2{position:absolute;left:611px;width:417px;top:53px;text-align:center;font-size:24px;font-weight:400;color:var(--navy)}
.field{position:absolute;height:33px;border:1px solid #9ab2d3;background:#f1f5fa;color:var(--navy);font-size:13px;padding:7px 14px}
.send{position:absolute;left:753px;top:292px;width:135px;height:37px;background:var(--navy);color:var(--white);font-size:12px;font-weight:700;text-align:center;line-height:37px;letter-spacing:.3px}

/* social + newsletter */
.subscribe{top:2734px;height:131px;background:var(--navy)}
.social{position:absolute;left:0;top:0;width:454px;height:131px;background:var(--cyan);color:var(--white);text-align:center}
.social h5{position:absolute;top:22px;width:100%;font-size:12px;font-weight:700;letter-spacing:.6px}
.social .circ{position:absolute;top:47px;width:30px;height:30px;border-radius:50%;background:rgba(255,255,255,.3)}
.social p{position:absolute;top:92px;width:100%;font-size:11.5px}
.news-text{position:absolute;left:454px;width:600px;top:32px;text-align:center;color:var(--white);font-size:12px}
.news-input{position:absolute;left:511px;top:67px;width:408px;height:31px;background:#0a3d7e;border:1px solid #2d62a8;color:#d6e1f0;font-size:11.5px;padding:8px 10px}
.go{position:absolute;left:955px;top:66px;width:33px;height:33px;border-radius:50%;background:var(--cyan);color:var(--white);font-size:11px;font-weight:700;text-align:center;line-height:33px}

/* footer */
.site-footer{top:2865px;height:408px;background:var(--footer);color:var(--footer-text);font-size:11px}
.site-footer h6{position:absolute;top:69px;font-size:12px;font-weight:700;color:var(--white);letter-spacing:.5px}
.contact-row{position:absolute;left:177px;display:flex;align-items:center;gap:18px}
.contact-row .ic{width:28px;height:28px;border-radius:50%;background:var(--navy);display:flex;align-items:center;justify-content:center}
.pill{position:absolute;height:22px;border:1px solid #33465f;font-size:10.5px;line-height:20px;padding:0 14px;letter-spacing:.4px}
.deal{position:absolute;left:615px;width:195px;font-size:11px;display:flex;justify-content:space-between;border-bottom:1px solid #2c405a;padding-bottom:5px}
.page-widget{position:absolute;left:831px;top:70px;width:197px;height:174px;background:var(--white)}
.page-widget .ph{position:absolute;left:6px;top:6px;width:185px;height:80px;background:linear-gradient(135deg,#c98a4b,#7b4a2d 60%,#3d5f8f)}
.page-widget .row{position:absolute;left:8px;height:6px;background:#d8dce2}
.page-widget .thumbs{position:absolute;left:8px;top:144px;display:flex;gap:3px}
.page-widget .thumbs i{width:18px;height:18px;background:#c9ccd2}
.foot-divider{position:absolute;left:172px;top:277px;width:856px;height:1px;background:#2e4360}
.copyright{position:absolute;left:183px;top:305px;color:#c7cfdb;font-size:11px}
.cards{position:absolute;left:799px;top:302px;display:flex;gap:4px}
.cards i{width:42px;height:24px;background:#e4e7ec;border-radius:2px}
</style>
</head>
<body>

<header class="hero">
  <div class="hero-photo" role="img" aria-label="Snow-covered mountain range under a pale sky with a powered hang glider flying across it"></div>
  <div class="topbar">
    <span style="left:182px">☏ +00 000 000 0000</span>
    <span style="left:360px">✉ info@briskfern.com</span>
    <span style="left:889px">Stay in Touch</span>
    <i class="abs dot" style="left:990px"></i>
    <i class="abs dot" style="left:1006px"></i>
  </div>
  <div class="logo"><span class="logo-mark"></span><span class="logo-name">Brisk Fern</span></div>
  <nav class="nav"><span>HOME</span><span>ABOUT</span><span>SERVICE</span><span>PRODUCTS</span><span>MY ACCOUNT</span><span>CONTACT</span></nav>
  <h1 class="hero-title">Rise to greater heights</h1>
</header>

<section class="products">
  <h2 class="sec-title" style="top:32px">OUR PRODUCTS</h2>
  <p class="sec-sub" style="top:78px">Sed ut perspiciatis unde omnis iste natus error sit voluptatem accusantium doloremque laudantium, totam rem aperiam</p>
  <div class="divider" style="top:135px"><i></i></div>

  <div class="product" style="left:172px">
    <div class="product-photo" role="img" aria-label="Yellow microlight aircraft with a striped wing against a deep blue sky" style="background:linear-gradient(180deg,#1b2f7a 0%,#3e5aa8 55%,#a8b5cc 80%,#e9edf2 100%)"></div>
    <div class="product-name">MICROLIGHT<br>AIRCRAFT</div>
  </div>
  <div class="product" style="left:465px">
    <div class="product-photo" role="img" aria-label="Two-seat powered hang glider with a red wing parked on an airfield" style="background:linear-gradient(180deg,#6f9fd6 0%,#b9cbe0 35%,#8a9470 60%,#4f5a3d 100%)"></div>
    <div class="product-name">2-SEAT POWERED HANG<br>GLIDER AND CATERS</div>
  </div>
  <div class="product" style="left:757px">
    <div class="product-photo" role="img" aria-label="Powered hang glider flying over red canyon rock formations" style="background:linear-gradient(180deg,#e9eef4 0%,#d8a070 40%,#b4552e 70%,#6e2c16 100%)"></div>
    <div class="product-name">POWERED<br>HANG GLIDER</div>
  </div>
</section>

<section class="why">
  <div class="why-photo" role="img" aria-label="Pilot flying a hang glider over a forested valley"></div>
  <h2 class="sec-title">WHY CHOOSE US</h2>
  <p class="sec-sub">Accusantium doloremque laudantium, totam rem aperiam</p>
  <div class="divider"></div>

  <div class="feature" style="left:393px">
    <div class="feature-icon"><svg width="64" height="64" viewBox="0 0 64 64" fill="none" stroke="#fff" stroke-width="2"><rect x="21" y="21" width="22" height="22"/><polyline points="24,38 30,31 34,34 40,26"/></svg></div>
    <h3>15 YEARS EXPERIENCE</h3><div class="rule"></div>
    <p>Sed quia consequuntur magni dolores eos qui ratione</p>
    <div class="btn-sm">READ MORE</div>
  </div>
  <div class="feature" style="left:613px">
    <div class="feature-icon"><svg width="64" height="64" viewBox="0 0 64 64" fill="none" stroke="#fff" stroke-width="2"><circle cx="32" cy="30" r="10"/><circle cx="32" cy="30" r="5"/><polyline points="26,38 24,46 32,42 40,46 38,38"/></svg></div>
    <h3>QUALITY PRODUCT</h3><div class="rule"></div>
    <p>Neque porro quisquam est qui dolorem ipsum</p>
    <div class="btn-sm">READ MORE</div>
  </div>
  <div class="feature" style="left:833px">
    <div class="feature-icon"><svg width="64" height="64" viewBox="0 0 64 64" fill="none" stroke="#fff" stroke-width="2"><circle cx="32" cy="32" r="12"/><text x="32" y="38" text-anchor="middle" fill="#fff" stroke="none" font-family="Lato,sans-serif" font-size="16" font-weight="700">$</text></svg></div>
    <h3>UNBEATABLE VALUE</h3><div class="rule"></div>
    <p>Sed quia consequuntur magni dolores eos qui ratione</p>
    <div class="btn-sm">READ MORE</div>
  </div>
</section>

<section class="blog">
  <h2 class="sec-title">LATEST FROM BLOG</h2>
  <p class="sec-sub">Adipisci velit, sed quia non numquam eius modi tempora incidunt ut laboredolor</p>
  <div class="divider" style="top:119px"><i></i></div>
  <div class="arrows">
    <span><svg width="8" height="10" viewBox="0 0 8 10" fill="none" stroke="#777" stroke-width="1.5"><polyline points="6,1 2,5 6,9"/></svg></span>
    <span><svg width="8" height="10" viewBox="0 0 8 10" fill="none" stroke="#777" stroke-width="1.5"><polyline points="2,1 6,5 2,9"/></svg></span>
  </div>

  <article class="post" style="left:172px">
    <div class="post-photo" role="img" aria-label="Microlight aircraft on skis in front of a hangar in the snow" style="background:linear-gradient(180deg,#cdd5df 0%,#e8ecf1 45%,#f7f8fa 100%)"></div>
    <div class="post-meta"><span>25 Apr, 2016</span><span>By Admin</span></div>
    <h4>Quis nostrum exercitationem</h4>
    <p>Ullam corporis suscipit laboriosam, nisi ut aliquid ex ea commodi consequatur autem vel eum iure reprehenderit qui in ea voluptate</p>
    <a>Read more</a>
  </article>
  <article class="post" style="left:465px">
    <div class="post-photo" role="img" aria-label="Pilot gliding above a green forested valley" style="background:linear-gradient(180deg,#dfe7ee 0%,#7c9a6a 40%,#3f6a3a 100%)"></div>
    <div class="post-meta"><span>14 Apr, 2016</span><span>By Admin</span></div>
    <h4>Ut enim ad minima veniam</h4>
    <p>Beatae vitae dicta sunt explicabo. Nemo enim ipsam voluptatem quia voluptas sit aspernatur aut odit aut fugit, sed quia conseq dolores</p>
    <a>Read more</a>
  </article>
  <article class="post" style="left:757px">
    <div class="post-photo" role="img" aria-label="Microlight flying over a blue lake and mountains" style="background:linear-gradient(180deg,#3b68b8 0%,#6e95cf 45%,#2f6d9a 75%,#25506e 100%)"></div>
    <div class="post-meta"><span>08 Apr, 2016</span><span>By Admin</span></div>
    <h4>Quis nostrum exercitationem</h4>
    <p>Ullam corporis suscipit laboriosam, nisi ut aliquid ex ea commodi consequatur autem vel eum iure reprehenderit qui in ea voluptate</p>
    <a>Read more</a>
  </article>
</section>

<section class="banner">We have supplied over 200 expedition-quality aircraft world-wide for 15 years.</section>

<section class="contact">
  <div class="contact-photo" role="img" aria-label="Red microlight flying low over a snowy mountain slope"></div>
  <h2>GET IN TOUCH</h2>
  <div class="field" style="left:611px;top:98px;width:204px">Name</div>
  <div class="field" style="left:824px;top:98px;width:204px">Subject</div>
  <div class="field" style="left:611px;top:137px;width:204px">Email</div>
  <div class="field" style="left:824px;top:137px;width:204px">Phone</div>
  <div class="field" style="left:611px;top:179px;width:417px;height:97px">Message</div>
  <div class="send">SEND MESSAGE</div>
</section>

<section class="subscribe">
  <div class="social">
    <h5>SOCIAL MEDIA</h5>
    <i class="circ" style="left:262px"></i>
    <i class="circ" style="left:310px"></i>
    <p>Stay in Touch via Social Networks</p>
  </div>
  <p class="news-text">Submit your email address and get latest updates and offers from us.</p>
  <div class="news-input">Enter mail address...</div>
  <div class="go">GO</div>
</section>

<footer class="site-footer">
  <h6 style="left:177px">ABOUT US</h6>
  <div class="contact-row" style="top:100px">
    <span class="ic"><svg width="12" height="14" viewBox="0 0 12 14" fill="#fff"><path d="M6 0a5 5 0 0 1 5 5c0 4-5 9-5 9S1 9 1 5a5 5 0 0 1 5-5zm0 3a2 2 0 1 0 0 4 2 2 0 0 0 0-4z"/></svg></span>
    <span>412 Alder Lane<br>Cedar Hollow, IL 60099</span>
  </div>
  <div class="contact-row" style="top:147px">
    <span class="ic"><svg width="12" height="12" viewBox="0 0 12 12" fill="#fff"><path d="M2.5 0l2 3-1.2 1.4a7 7 0 0 0 4.3 4.3L9 7.5l3 2-1.3 2.2C5 11.5.5 7 .3 1.3z"/></svg></span>
    <span>+00 000 000 0000</span>
  </div>
  <div class="contact-row" style="top:195px">
    <span class="ic"><svg width="13" height="10" viewBox="0 0 13 10" fill="none" stroke="#fff" stroke-width="1.3"><rect x=".7" y=".7" width="11.6" height="8.6"/><polyline points=".7,.7 6.5,5.5 12.3,.7"/></svg></span>
    <span>info@briskfern.com</span>
  </div>

  <h6 style="left:395px">LINKS</h6>
  <span class="pill" style="left:395px;top:98px">DEALS</span>
  <span class="pill" style="left:475px;top:98px">GALLERY</span>
  <span class="pill" style="left:395px;top:125px">BLOG</span>
  <span class="pill" style="left:470px;top:125px">SHIPPING INFO</span>
  <span class="pill" style="left:395px;top:152px">TERMS &amp; CONDITIONS</span>
  <span class="pill" style="left:395px;top:179px">PRIVACY POLICY</span>

  <h6 style="left:615px">LATEST DEALS</h6>
  <div class="deal" style="top:96px"><span>Quis nostrum exercit</span><span>›</span></div>
  <div class="deal" style="top:123px"><span>Ullam corporis suscipit</span><span>›</span></div>
  <div class="deal" style="top:151px"><span>Commodi consequatur</span><span>›</span></div>
  <div class="deal" style="top:179px"><span>Dolores eos qui ratione</span><span>›</span></div>
  <div class="deal" style="top:205px"><span>Quaerat voluptatem</span><span>›</span></div>

  <div class="page-widget" role="img" aria-label="Social page preview with a cover photo and follower thumbnails">
    <div class="ph"></div>
    <div class="row" style="top:96px;width:90px"></div>
    <div class="row" style="top:110px;width:150px"></div>
    <div class="row" style="top:124px;width:120px"></div>
    <div class="thumbs"><i></i><i></i><i></i><i></i><i></i><i></i><i></i><i></i></div>
  </div>

  <div class="foot-divider"></div>
  <p class="copyright">Copyright © 2016 Brisk Fern</p>
  <div class="cards"><i></i><i></i><i></i><i></i><i></i></div>
</footer>

</body>
</html>
```